Disposable Mini Sauce Pot Design for Asian Chain Food Brands

We operate a Hainan Chicken Rice takeout brand under the name Wokly8, with our official website: www.Wokly8.com.
We offer four signature house sauces and are launching brand-new packaging for our sauce line. We require custom graphic designs exclusively for the sauce cup lids.
Product Material & Base Specs
The sauce cups are made of PP plastic, available in two translucent base options: Translucent White and Translucent Orange.
Four Sauce Varieties for Individual Lid Designs
1. Red Sauce – Fried Sweet Chili Sauce
2.Green Sauce – Scallion Oil Dressing
3.Sweet Soy Sauce
4.Sweet Red Sauce (Special for Fried Chicken)
Differentiate each sauce lid design through unique graphics, typography, or illustrative elements for easy customer identification.
The marking NET WT 2 OZ must be clearly printed on every lid.
**There is no need to print full descriptive text or the full name of the sauces on each lid; the design only needs to clearly differentiate the four sauce varieties.
**Please reference the original design style and brand color palette shown on our official website, and feel free to fully unleash your creativity.
Look and feel
Each slider illustrates characteristics of the customer's brand and the style your logo design should communicate.

```html
<!DOCTYPE html>
<html lang="en">
<head>
<meta charset="utf-8">
<title>Wokly8 Sauce Lid Set</title>
<link rel="stylesheet" href="https://fonts.googleapis.com/css2?family=Barlow+Semi+Condensed:wght@600;700&display=swap">
<style>
  :root {
    --page: #ffffff;
    --lid-chili: #c20404;
    --lid-scallion: #33a300;
    --lid-soy: #2b1a0f;
    --lid-fried: #900200;
    --line: #ffffff;
    --accent-yellow: #f1d219;
    --font-brand: "Barlow Semi Condensed", "Arial Narrow", sans-serif;
  }
  html, body {
    margin: 0;
    padding: 0;
    width: 1200px;
    height: 1200px;
    overflow: hidden;
    background: var(--page);
  }
  .lid-sheet {
    position: relative;
    width: 1200px;
    height: 1200px;
  }
  .lid {
    position: absolute;
    width: 461px;
    height: 461px;
    border-radius: 52px;
    box-shadow: 0 26px 34px -6px rgba(0, 0, 0, 0.38);
    color: var(--line);
    font-family: var(--font-brand);
  }
  .lid--chili    { left: 97px;  top: 102px; background: var(--lid-chili); }
  .lid--scallion { left: 655px; top: 102px; background: var(--lid-scallion); }
  .lid--soy      { left: 81px;  top: 628px; background: var(--lid-soy); }
  .lid--fried    { left: 654px; top: 630px; background: var(--lid-fried); }

  .lid__frame {
    position: absolute;
    inset: 16px;
    border: 2px solid var(--line);
    border-radius: 38px;
  }
  .lid__art {
    position: absolute;
    inset: 0;
    width: 461px;
    height: 461px;
  }
  .lid__brand-top {
    position: absolute;
    top: 36px;
    left: 0;
    right: 0;
    text-align: center;
    font-weight: 700;
    font-size: 34px;
    line-height: 1;
    letter-spacing: 0.5px;
  }
  .lid__brand-main {
    position: absolute;
    top: 318px;
    left: 0;
    right: 0;
    text-align: center;
    font-weight: 700;
    font-size: 50px;
    line-height: 1;
    letter-spacing: 0.5px;
  }
  .lid__underline {
    position: absolute;
    top: 377px;
    left: 160px;
    width: 142px;
    height: 4px;
    border-radius: 2px;
    background: var(--accent-yellow);
  }
  .lid__weight {
    position: absolute;
    top: 398px;
    left: 0;
    right: 0;
    text-align: center;
    font-weight: 700;
    font-size: 19px;
    line-height: 1;
    letter-spacing: 0.3px;
  }
</style>
</head>
<body>
<main class="lid-sheet">

  <section class="lid lid--chili" aria-label="Sweet chili sauce lid">
    <div class="lid__frame"></div>
    <svg class="lid__art" viewBox="0 0 461 461">
      <defs>
        <linearGradient id="chili-tones" x1="0" y1="1" x2="1" y2="0">
          <stop offset="0" stop-color="#e3100a"/>
          <stop offset="0.55" stop-color="#f23a2a"/>
          <stop offset="0.8" stop-color="#7fd63a"/>
          <stop offset="1" stop-color="#58c21e"/>
        </linearGradient>
      </defs>
      <g fill="none" stroke="#ffffff" stroke-opacity="0.75" stroke-width="1.5">
        <circle cx="40" cy="127" r="7"/><circle cx="72" cy="170" r="9"/>
        <circle cx="383" cy="150" r="9"/><circle cx="363" cy="179" r="5"/>
        <circle cx="40" cy="331" r="5"/><circle cx="114" cy="66" r="5"/>
      </g>
      <circle cx="228" cy="204" r="104" fill="none" stroke="#ffffff" stroke-width="5"/>
      <circle cx="228" cy="204" r="80" fill="url(#chili-tones)" role="img" aria-label="Red chili pepper with green stem illustration"/>
    </svg>
    <div class="lid__brand-top">Wokly8</div>
    <div class="lid__brand-main">Wokly8</div>
    <div class="lid__underline"></div>
    <div class="lid__weight">NET WT 2 OZ</div>
  </section>

  <section class="lid lid--scallion" aria-label="Scallion oil dressing lid">
    <div class="lid__frame"></div>
    <svg class="lid__art" viewBox="0 0 461 461">
      <defs>
        <linearGradient id="scallion-tones" x1="0" y1="1" x2="1" y2="0">
          <stop offset="0" stop-color="#f4f8ec"/>
          <stop offset="0.35" stop-color="#c9f0a4"/>
          <stop offset="0.7" stop-color="#5fd12a"/>
          <stop offset="1" stop-color="#2f9a00"/>
        </linearGradient>
      </defs>
      <g fill="none" stroke="#ffffff" stroke-opacity="0.45" stroke-width="1.5">
        <circle cx="40" cy="127" r="7"/><circle cx="72" cy="170" r="9"/>
        <circle cx="383" cy="150" r="9"/><circle cx="363" cy="179" r="5"/>
        <circle cx="40" cy="331" r="5"/><circle cx="114" cy="66" r="5"/>
      </g>
      <circle cx="228" cy="204" r="104" fill="none" stroke="#ffffff" stroke-width="5"/>
      <circle cx="228" cy="204" r="80" fill="url(#scallion-tones)" role="img" aria-label="Green scallion with white bulb illustration"/>
    </svg>
    <div class="lid__brand-top">Wokly8</div>
    <div class="lid__brand-main">Wokly8</div>
    <div class="lid__underline"></div>
    <div class="lid__weight">NET WT 2 OZ</div>
  </section>

  <section class="lid lid--soy" aria-label="Sweet soy sauce lid">
    <div class="lid__frame"></div>
    <svg class="lid__art" viewBox="0 0 461 461">
      <g fill="none" stroke="#ffffff" stroke-opacity="0.75" stroke-width="1.5">
        <circle cx="40" cy="127" r="7"/><circle cx="72" cy="170" r="9"/>
        <circle cx="383" cy="150" r="9"/><circle cx="363" cy="179" r="5"/>
        <circle cx="40" cy="331" r="5"/><circle cx="114" cy="66" r="5"/>
      </g>
      <circle cx="228" cy="204" r="104" fill="none" stroke="#ffffff" stroke-width="5"/>
      <path d="M228 132 C 210 170, 184 192, 184 222 A 44 44 0 0 0 272 222 C 272 192, 246 170, 228 132 Z" fill="#ffffff"/>
      <path d="M202 218 C 200 240, 210 252, 232 254" fill="none" stroke="#2b1a0f" stroke-width="5" stroke-linecap="round"/>
    </svg>
    <div class="lid__brand-top">Wokly8</div>
    <div class="lid__brand-main">Wokly8</div>
    <div class="lid__underline"></div>
    <div class="lid__weight">NET WT 2 OZ</div>
  </section>

  <section class="lid lid--fried" aria-label="Sweet red sauce for fried chicken lid">
    <div class="lid__frame"></div>
    <svg class="lid__art" viewBox="0 0 461 461">
      <g fill="none" stroke="#ffffff" stroke-opacity="0.75" stroke-width="1.5">
        <circle cx="40" cy="127" r="7"/><circle cx="72" cy="170" r="9"/>
        <circle cx="383" cy="150" r="9"/><circle cx="363" cy="179" r="5"/>
        <circle cx="40" cy="331" r="5"/><circle cx="114" cy="66" r="5"/>
      </g>
      <circle cx="228" cy="204" r="104" fill="none" stroke="#ffffff" stroke-width="5"/>
      <path class="lid__flame-icon" d="M236 130 C 262 160, 282 182, 282 222 C 282 256, 258 276, 228 276 C 198 276, 174 256, 174 226 C 174 204, 186 190, 198 178 C 198 196, 204 208, 214 212 C 208 186, 218 156, 236 130 Z M228 268 C 246 268, 256 254, 256 240 C 256 222, 242 210, 236 196 C 232 212, 222 218, 214 226 C 206 234, 202 242, 202 248 C 202 260, 212 268, 228 268 Z" fill="#ffffff" fill-rule="evenodd" role="img" aria-label="Flame icon for fried chicken sauce"/>
    </svg>
    <div class="lid__brand-top">Wokly8</div>
    <div class="lid__brand-main">Wokly8</div>
    <div class="lid__underline"></div>
    <div class="lid__weight">NET WT 2 OZ</div>
  </section>

</main>
</body>
</html>
```